Digital content business needs banner ads

We sell content - if you need an article to put on your website or in a newsletter, you can purchase a ready made article from us and edit it to your liking to use straight away. This could be any kind of article, but this banner ad will be aimed at real estate agents. You can see the website (and the style of articles) here https://www.thebluelanternpost.com.au
The banner is meant to solve the problem of the front desk admin or agent trying to think of something to write to put in their email newsletter. This will save them time as they can just select an article from our library and use it (for a fee of course!).
Needs to have the words:
--------------------------------------------------
Find the next article for your newsletter
---------------------------------------------------
Some imagery would be good rather than plain text.
With a call to action like click here button or similar
Required sizes (or provide a set of standard sized ads):
728 x 90
970 x 250
300x250
Real Estate Agents

```html
<!DOCTYPE html>
<html lang="en">
<head>
<meta charset="utf-8">
<title>The Blue Lantern Post – Find the next article</title>
<link rel="stylesheet" href="https://fonts.googleapis.com/css2?family=Roboto:wght@400;700;900&display=swap">
<style>
  :root {
    --bg-light: #f4f4f3;
    --bg-mid: #dcdcda;
    --ink: #1f2326;
    --ink-soft: #2b2f33;
    --brand-blue: #1b8fd8;
    --brand-navy: #174a7c;
    --button-top: #1d93dc;
    --button-bottom: #0f6fb6;
    --white: #ffffff;
  }
  * { margin: 0; padding: 0; box-sizing: border-box; }
  html, body { width: 1200px; height: 148px; overflow: hidden; }
  body { font-family: "Roboto", Arial, sans-serif; }

  .banner {
    position: relative;
    width: 1200px;
    height: 148px;
    overflow: hidden;
    background: linear-gradient(90deg, var(--bg-light) 0%, #ececea 55%, var(--bg-mid) 100%);
  }

  .brand {
    position: absolute;
    left: 32px;
    top: 34px;
    width: 170px;
    display: flex;
    align-items: center;
    gap: 10px;
  }
  .brand-square {
    flex: none;
    width: 22px;
    height: 22px;
    background: var(--brand-blue);
  }
  .brand-name {
    font-weight: 900;
    font-size: 20px;
    line-height: 1.1;
    color: var(--brand-navy);
  }

  .headline {
    position: absolute;
    left: 214px;
    top: 28px;
    font-weight: 700;
    font-size: 44px;
    line-height: 1;
    letter-spacing: -0.3px;
    color: var(--ink);
  }
  .headline .accent { color: var(--brand-blue); }

  .subline {
    position: absolute;
    left: 214px;
    top: 82px;
    font-weight: 400;
    font-size: 31px;
    line-height: 1;
    color: var(--ink-soft);
  }

  .agent-photo {
    position: absolute;
    left: 775px;
    top: 0;
    width: 215px;
    height: 148px;
    background: radial-gradient(ellipse at 50% 60%, #ffffff 0%, #e9e9e7 55%, rgba(220,220,218,0) 80%);
  }

  .cta {
    position: absolute;
    left: 968px;
    top: 38px;
    width: 205px;
    height: 74px;
    display: flex;
    align-items: center;
    justify-content: center;
    background: linear-gradient(180deg, var(--button-top), var(--button-bottom));
    color: var(--white);
    font-weight: 700;
    font-size: 26px;
    letter-spacing: 0.3px;
    text-decoration: none;
  }
</style>
</head>
<body>
  <div class="banner">
    <a class="brand" href="https://www.thebluelanternpost.com.au">
      <span class="brand-square"></span>
      <span class="brand-name">The Blue Lantern Post</span>
    </a>

    <h1 class="headline">Find the <span class="accent">next article</span></h1>
    <p class="subline">for your newsletter</p>

    <div class="agent-photo" role="img" aria-label="Smiling real estate agent in a white shirt and tie presenting a small model house"></div>

    <a class="cta" href="https://www.thebluelanternpost.com.au">KNOW MORE</a>
  </div>
</body>
</html>
```